New Website for Belcourt Manor at www.belcourt.com.au

A new logo has been designed (through pixel forge) and we now want to align the look and feel of our website at www.belcourt.com.au to the new logo. The content and page names (e.g. Grounds) will remain largely unchanged for the new site, so please submit a new look "Home" page, using our new logo, current text and any photos you choose from the existing gallery at our website. I have also attached the current "Home" page photos.

Industry/Entity Type

Accommodation

Number of Pages Required

1 page

Requirements
Must have
• Logo to be presented on white background.

```html
<!DOCTYPE html>
<html lang="en">
<head>
<meta charset="utf-8">
<title>Belcourt Manor – Home</title>
<link href="https://fonts.googleapis.com/css2?family=Montserrat:wght@300;400;500;600&family=Great+Vibes&display=swap" rel="stylesheet">
<style>
:root{
  --blue:#0e9ad9;
  --blue-dark:#0b6fb0;
  --script-blue:#1a8fd0;
  --gold:#f2c81e;
  --ink:#2b2b2b;
  --text:#444;
  --white:#fff;
  --footer:#262626;
  --footer-base:#1a1a1a;
  --tile-overlay:rgba(0,0,0,.35);
}
*{margin:0;padding:0;box-sizing:border-box}
html,body{width:1200px;height:3659px;overflow:hidden}
body{font-family:"Montserrat",Arial,sans-serif;color:var(--text);background:var(--white);position:relative}
.section{position:absolute;left:0;width:1200px}
.eyebrow{font-size:20px;letter-spacing:1px;color:var(--ink);text-align:center;font-weight:400;text-transform:uppercase}
.script{font-family:"Great Vibes",cursive;color:var(--script-blue);font-size:56px;text-align:center;font-weight:400;line-height:1.1}

/* hero */
.hero{top:0;height:659px;overflow:hidden}
.hero-photo{position:absolute;inset:0;background:
  radial-gradient(ellipse 420px 160px at 640px 250px,rgba(255,214,140,.75),rgba(255,214,140,0) 70%),
  linear-gradient(90deg,rgba(60,38,22,.9) 0%,rgba(120,70,35,.55) 22%,rgba(0,0,0,0) 34%),
  linear-gradient(180deg,#8fa1b3 0%,#c9b49a 22%,#e2a867 34%,#8a8a6e 44%,#5e6e58 52%,#7a5c44 64%,#4a3a2e 80%,#2b241f 100%)}
.brand-plate{position:absolute;top:52px;left:50%;transform:translateX(-50%);background:var(--white);padding:26px 44px;display:flex;align-items:center;gap:18px;box-shadow:0 6px 24px rgba(0,0,0,.18)}
.brand-dot{width:42px;height:42px;border-radius:50%;background:var(--blue)}
.brand-name{font-family:"Montserrat",Arial,sans-serif;font-weight:500;font-size:58px;color:var(--blue);letter-spacing:1px;line-height:1;white-space:nowrap}
.nav{position:absolute;top:596px;left:0;width:1200px;height:63px;background:rgba(20,20,22,.72);display:flex;justify-content:center;align-items:center;gap:46px}
.nav a{color:var(--white);text-decoration:none;font-size:16px;letter-spacing:.5px;text-transform:uppercase}
.nav a.active{color:var(--blue)}

/* about */
.about{top:659px;height:341px}
.about .eyebrow{margin-top:55px}
.about .script{margin-top:8px}
.about p{width:860px;margin:20px auto 0;text-align:center;font-size:14px;line-height:24px;color:#333}

/* testimonials */
.testimonials{top:1000px;height:520px;background:
  radial-gradient(ellipse 500px 140px at 600px 330px,rgba(120,110,70,.35),rgba(0,0,0,0) 70%),
  linear-gradient(180deg,#1e2a36 0%,#3c4c5c 22%,#5c6874 38%,#3e4a3a 52%,#3f3d22 70%,#2e2a18 100%)}
.testimonials .eyebrow{color:var(--white);margin-top:55px}
.testimonials .script{margin-top:6px}
.quote-mark{position:absolute;top:175px;left:573px;width:54px;height:54px;border:3px solid var(--gold);border-radius:50%;color:var(--gold);font-size:40px;font-weight:600;text-align:center;line-height:60px}
.testimonials blockquote{position:absolute;top:255px;left:180px;width:840px;text-align:center;color:var(--white);font-size:14px;line-height:25px}
.reviewer{position:absolute;top:362px;left:470px;display:flex;align-items:center;gap:24px}
.avatar{width:86px;height:86px;border-radius:50%;background:linear-gradient(160deg,#d8c2a8,#8f7560);border:3px solid var(--white)}
.reviewer-name{color:var(--gold);font-size:18px}
.reviewer-role{color:var(--white);font-size:14px;margin-top:10px}
.arrow-btn{position:absolute;top:382px;width:42px;height:42px;border:2px solid rgba(255,255,255,.8);border-radius:50%}
.arrow-btn svg{display:block}

/* services */
.services{top:1520px;height:617px}
.services .eyebrow{margin-top:62px}
.services .script{margin-top:4px}
.tile{position:absolute;width:334px;height:186px;display:flex;align-items:center;justify-content:center}
.tile span{position:relative;color:var(--white);font-size:22px;text-transform:uppercase;letter-spacing:.5px}
.tile span.highlight{color:var(--gold)}
.tile::before{content:"";position:absolute;inset:0;background:var(--tile-overlay)}

/* search */
.search{top:2137px;height:144px;background:var(--blue)}
.search-input{position:absolute;top:48px;left:273px;width:520px;height:50px;border:2px solid rgba(255,255,255,.85);color:rgba(255,255,255,.85);font-size:13px;line-height:46px;padding-left:18px;text-transform:uppercase}
.search-btn{position:absolute;top:48px;left:803px;width:124px;height:50px;background:var(--blue-dark);color:var(--white);font-size:16px;font-weight:500;text-align:center;line-height:50px;text-transform:uppercase}
.search-pointer{position:absolute;top:143px;left:576px}

/* properties */
.properties{top:2281px;height:178px}
.properties .eyebrow{margin-top:72px}
.properties .script{margin-top:4px}
.gallery{top:2459px;height:371px;display:grid;grid-template-columns:repeat(4,300px);grid-template-rows:185px 186px}
.map{top:2830px;height:548px;background:
  radial-gradient(ellipse 260px 200px at 90px 260px,#a9cbe6 0%,#a9cbe6 55%,rgba(169,203,230,0) 72%),
  radial-gradient(ellipse 240px 300px at 1120px 260px,#b7d3ea 0%,rgba(183,211,234,0) 70%),
  radial-gradient(ellipse 300px 160px at 560px 200px,#d7e4c6 0%,rgba(215,228,198,0) 70%),
  linear-gradient(135deg,#ece9e2 0%,#e4e8da 45%,#e9e5db 75%,#d6e2ea 100%)}

/* footer */
.footer{top:3378px;height:212px;background:var(--footer);color:var(--white)}
.to-top{position:absolute;top:-22px;left:576px;width:48px;height:44px;background:#333}
.footer-col{position:absolute;top:0;text-align:center}
.footer-brand{left:84px;width:320px;top:44px}
.footer-brand .brand-name{font-size:30px;color:var(--white);font-weight:500}
.footer-brand address{font-style:normal;font-size:15px;line-height:24px;margin-top:22px}
.footer-follow{left:450px;width:300px;top:62px}
.footer-follow h3,.footer-contact h3{font-size:15px;font-weight:400;text-transform:uppercase;letter-spacing:.5px}
.socials{display:flex;justify-content:center;gap:12px;margin-top:24px}
.socials span{width:40px;height:40px;border:1px solid #555;display:block}
.socials span.primary{background:var(--blue);border-color:var(--blue)}
.footer-contact{left:833px;width:300px;top:30px;font-size:14px}
.footer-contact svg{display:block;margin:22px auto 8px}
.copyright{top:3590px;height:69px;background:var(--footer-base);color:#ccc;font-size:13px;text-align:center;line-height:69px}
.copyright b{color:var(--blue);font-weight:400}
</style>
</head>
<body>

<header class="section hero">
  <div class="hero-photo" role="img" aria-label="Sunset view from a mansion balcony with outdoor lounge, over a lake and suburban homes"></div>
  <div class="brand-plate"><span class="brand-dot"></span><span class="brand-name">Belcourt Manor</span></div>
  <nav class="nav">
    <a class="active" href="#">Home</a>
    <a href="#">Mansion</a>
    <a href="#">Gallery</a>
    <a href="#">Location</a>
    <a href="#">Availability</a>
    <a href="#">Contact</a>
  </nav>
</header>

<section class="section about">
  <h2 class="eyebrow">About</h2>
  <div class="script">Belcourt Manor</div>
  <p>On over 2 manicured garden acres, Belcourt Manor is a unique Coral Coast estate, centrally located in the prestigious rural suburb of Kestrel Vale. More about our Location<br>
  The estate features a grand mansion, private pub (The Fox and Hound), sparkling resort pool, tennis court and playground.<br>
  Magnificent properties rarely feel so warm and welcoming – so browse away and visit our photo gallery<br>
  – and we look forward to having you stay as our guests.<br>
  For prices, availability and guest reviews, visit StayHaven.</p>
</section>

<section class="section testimonials" role="img" aria-label="Countryside field with hay bales under a cloudy evening sky">
  <h2 class="eyebrow">What</h2>
  <div class="script">Our Clients Say</div>
  <div class="quote-mark">“</div>
  <blockquote>Lorem Ipsum is simply dummy text of the printing and typesetting industry. Lorem Ipsum has been the industry's standard dummy text ever since the 1500s, when an unknown printer took a galley of type and scrambled it to make a type specimen book. It has survived not only five centuries.</blockquote>
  <div class="reviewer">
    <div class="avatar" role="img" aria-label="Client portrait"></div>
    <div><div class="reviewer-name">Mira Collins</div><div class="reviewer-role">CEO, Company Name</div></div>
  </div>
  <div class="arrow-btn" style="left:352px"><svg width="38" height="38" viewBox="0 0 38 38"><path d="M22 12l-7 7 7 7" fill="none" stroke="#fff" stroke-width="2"/></svg></div>
  <div class="arrow-btn" style="left:803px"><svg width="38" height="38" viewBox="0 0 38 38"><path d="M16 12l7 7-7 7" fill="none" stroke="#fff" stroke-width="2"/></svg></div>
</section>

<section class="section services">
  <h2 class="eyebrow">Services</h2>
  <div class="script">We Provide</div>
  <div class="tile" style="left:78px;top:168px;background:linear-gradient(180deg,#3f5a34 0%,#9a5a3c 40%,#b07a5a 60%,#6a6a5a 80%,#4a4a40 100%)" role="img" aria-label="Mansion exterior with gardens"><span class="highlight">Mansion</span></div>
  <div class="tile" style="left:434px;top:168px;background:linear-gradient(180deg,#6a5e52 0%,#8a7a68 40%,#a88a66 60%,#6a4a34 85%,#3e2e24 100%)" role="img" aria-label="Guest bedroom"><span>Bedrooms</span></div>
  <div class="tile" style="left:790px;top:168px;background:linear-gradient(180deg,#5e5650 0%,#7a6a5a 40%,#a0704a 60%,#4a3a30 85%,#2e2a28 100%)" role="img" aria-label="Living room"><span>Options</span></div>
  <div class="tile" style="left:78px;top:378px;background:linear-gradient(180deg,#4a3e34 0%,#6a5040 40%,#8a5a34 60%,#3a2a20 85%,#221a16 100%)" role="img" aria-label="Private pub interior"><span>Fox &amp; Hound</span></div>
  <div class="tile" style="left:434px;top:378px;background:linear-gradient(180deg,#7a8a8a 0%,#5a6a5a 35%,#4e6048 60%,#6a7a70 80%,#3a4a40 100%)" role="img" aria-label="Estate grounds and pool"><span>Grounds</span></div>
  <div class="tile" style="left:790px;top:378px;background:linear-gradient(180deg,#8a9a9a 0%,#5a7048 35%,#4a6a36 60%,#5e7a40 80%,#3a5028 100%)" role="img" aria-label="Garden wedding lawn"><span>DIY Weddings</span></div>
</section>

<section class="section search">
  <div class="search-input">Find luxury resort &amp; estates by locations</div>
  <div class="search-btn">Search</div>
  <svg class="search-pointer" width="48" height="24" viewBox="0 0 48 24"><path d="M0 0h48L24 24z" fill="#0e9ad9"/></svg>
</section>

<section class="section properties">
  <h2 class="eyebrow">Proprties</h2>
  <div class="script">Wattle Creek Showground</div>
</section>

<section class="section gallery">
  <div role="img" aria-label="Young riders in equestrian helmets" style="background:linear-gradient(180deg,#8a8a8a 0%,#3a3a44 35%,#1e2236 65%,#5a4030 100%)"></div>
  <div role="img" aria-label="Bicycles at the showground, highlighted" style="background:linear-gradient(180deg,#2a8ac8 0%,#1f7fb8 50%,#3aa0d8 100%)"></div>
  <div role="img" aria-label="Child on a colourful slide" style="background:linear-gradient(90deg,#c86a2a 0%,#8aa03a 35%,#d07a3a 65%,#8a9aa8 100%)"></div>
  <div role="img" aria-label="Market stall visitors" style="background:linear-gradient(180deg,#e0ddd8 0%,#c8b8a8 45%,#a05a50 75%,#5a4a48 100%)"></div>
  <div role="img" aria-label="Camel ride at the show" style="background:linear-gradient(180deg,#6a7a8a 0%,#5a4a3a 45%,#8a6a40 70%,#3a3028 100%)"></div>
  <div role="img" aria-label="Judge with clipboard on the lawn" style="background:linear-gradient(180deg,#c8d4dc 0%,#9ab08a 45%,#5a8a3a 75%,#4a7030 100%)"></div>
  <div role="img" aria-label="Showgoers greeting each other" style="background:linear-gradient(180deg,#6a8a5a 0%,#8a4a3a 45%,#c89a6a 70%,#4a3a30 100%)"></div>
  <div role="img" aria-label="Vintage tractor display" style="background:linear-gradient(180deg,#3a5030 0%,#2a3a22 35%,#b8402a 65%,#5a3a2a 100%)"></div>
</section>

<section class="section map" role="img" aria-label="Street map of the showground area and surrounding suburbs"></section>

<footer class="section footer">
  <div class="to-top"><svg width="48" height="44" viewBox="0 0 48 44"><path d="M14 28l10-11 10 11z" fill="#0e9ad9"/></svg></div>
  <div class="footer-col footer-brand">
    <div class="brand-name">Belcourt Manor</div>
    <address>19 Belcourt Drive<br>Kestrel Vale, Coral Coast<br>Queensland, Australia</address>
  </div>
  <div class="footer-col footer-follow">
    <h3>Follow Us</h3>
    <div class="socials"><span class="primary"></span><span></span><span></span></div>
  </div>
  <div class="footer-col footer-contact">
    <h3>Contact Us</h3>
    <svg width="22" height="22" viewBox="0 0 24 24"><path d="M6 3l3 4-2 2c1 3 4 6 7 7l2-2 4 3-2 4C10 21 3 14 2 5z" fill="none" stroke="#fff" stroke-width="1.5"/></svg>
    <div>1300 555 019</div>
    <svg width="22" height="18" viewBox="0 0 24 18"><rect x="1" y="1" width="22" height="16" fill="none" stroke="#fff" stroke-width="1.5"/><path d="M1 1l11 9 11-9" fill="none" stroke="#fff" stroke-width="1.5"/></svg>
    <div>WWW.BELCOURT.COM.AU</div>
  </div>
</footer>

<div class="section copyright">© <b>BELCOURT MANOR</b> 2016. All rights reserved.</div>

</body>
</html>
```